Journal Cover Design Project

The Worldwide Review of Rising Trade Systems is a professional journal which aims to provide an international platform for publication of original research on the emerging economies.
The journal is published three times a year and available by subscription. Currently, the cover design is the same for each issue. We are looking to redesign the cover (and interior) of our journal and would like a design that would allow us to change the color scheme for each issue or volume while maintaining a consistent design scheme.
Our design preference is simple and modern with good use of color. Many of our past publications have used abstract maps/globes but we are open to new ideas. We would need a creative way to include text on the cover, possibly a way to present the article titles or main topics for each issue. For example, we like the use of color and the general design in this image: http://www.pixmoravo.example/photos/drawdreamhope/5182640913/lightbox/
Below is a link to our most recent issue of the journal. You can see an example of the article titles, structure, etc. The website also shows the current cover of the journal (but we do not want the new design to be based off of the current one):
http://rts.quilberpress.example/content/4/2.toc

```html
<!DOCTYPE html>
<html lang="en">
<head>
<meta charset="utf-8">
<title>Trade and Transport in Central Asia — Interior Spread</title>
<link rel="stylesheet" href="https://fonts.googleapis.com/css2?family=Alegreya+Sans:wght@400;500;700&display=swap">
<style>
  :root {
    --backdrop: #2b3238;
    --paper: #ffffff;
    --ink: #2a2a2a;
    --heading-ink: #1e1e1e;
    --accent-red: #c8151f;
    --accent-red-dark: #8f0d14;
    --table-band: #dfe1ec;
    --table-head: #d4d7e3;
    --rule: #6b6f80;
  }
  * { margin: 0; padding: 0; box-sizing: border-box; }
  html, body {
    width: 1200px; height: 900px; overflow: hidden;
    background: var(--backdrop);
  }
  body {
    position: relative;
    font-family: "Alegreya Sans", "Trebuchet MS", sans-serif;
    color: var(--ink);
    font-variant-numeric: oldstyle-nums;
  }
  .spread {
    position: absolute; left: 25px; top: 42px;
    width: 1150px; height: 754px;
    background: var(--paper);
    display: flex;
  }
  .page { position: relative; width: 575px; height: 754px; overflow: hidden; }
  .body-copy {
    position: absolute;
    font-size: 12px; line-height: 17.4px;
    text-align: justify; hyphens: auto;
  }
  .body-copy p + p { margin-top: 17.4px; }
  .page--left .body-copy { left: 94px; width: 434px; top: 126px; }
  .page--right .body-copy { left: 48px; width: 435px; top: 75px; }
  .section-title {
    position: absolute; left: 94px; top: 69px;
    font-size: 19.5px; font-weight: 700; color: var(--heading-ink);
    letter-spacing: 0.2px;
  }
  .lead-in { font-weight: 700; letter-spacing: 0.3px; font-size: 11.5px; }

  .data-table { position: absolute; left: 0; top: 501px; width: 528px; }
  .data-table__caption {
    height: 23px; padding-left: 94px;
    background: linear-gradient(90deg, var(--accent-red-dark) 0%, var(--accent-red) 45%, var(--accent-red) 80%, var(--accent-red-dark) 100%);
    color: #fff; font-size: 13.5px; line-height: 23px;
  }
  .data-table__caption strong { font-weight: 700; }
  .data-table table { width: 100%; border-collapse: collapse; font-size: 10px; }
  .data-table th, .data-table td { height: 16.5px; padding: 0; }
  .data-table .row-group th {
    height: 25px; background: var(--table-band);
    font-weight: 400; font-size: 10.5px; text-align: center; padding-left: 20px;
  }
  .data-table .row-head th {
    height: 22px; background: var(--table-head); font-weight: 700; font-size: 10px;
  }
  .data-table .country { padding-left: 94px; text-align: left; width: 175px; }
  .data-table .year { text-align: right; width: 54px; }
  .data-table .year--b { width: 83px; }
  .data-table .exports { text-align: left; padding-left: 50px; }
  .data-table tbody tr:nth-child(even) td { background: var(--table-band); }
  .data-table tbody tr:last-child td { border-bottom: 8px solid var(--table-band); }
  .data-table table { border-bottom: 1px solid var(--rule); }

  .folio {
    position: absolute; top: 697px;
    font-size: 8.5px; letter-spacing: 0.6px; text-transform: uppercase;
    display: flex; align-items: center; gap: 7px;
  }
  .folio__num { font-weight: 700; font-variant-numeric: lining-nums; }
  .folio__mark { width: 7px; height: 7px; }
  .page--left .folio { left: 94px; }
  .page--right .folio { right: 90px; }
</style>
</head>
<body>
  <div class="spread">
    <section class="page page--left">
      <h1 class="section-title">1. INTRODUCTION</h1>
      <div class="body-copy">
        <p><span class="lead-in">UNTIL 1991, CENTRAL ASIA WAS PART</span> of the integrated economic space of the Soviet Union without borders Maximihil ta mor unum labus, sa re nem re culium ia L. Vivati, crisse pereo, publinteatum meisunt. Caesilis, caperce retiusque ad aurnit. Nihicap ecivid patimpl. Equam que ia? Ucia? quast nem, oca; nonsidees nir ut apero intiam hos vis. Sentimoraris ad firtus eredo, movidem senatus, vidienit, que caes sensus pribut idem hi, quem omnerte riamdiere antror quam. ehebem nos opublis ia nemus, st arit. Ec iam Patilica ver hortude neque fatum nonclus consupim noviri co vem sedo, unte, quiu itum tem et pribus conimis intis. Dermist racta, Catress iliquemei practua L. Voliculis Catum ta, publin videm nosus opopubit vis eorum qua publin se nuntese ia autes es pati se inunum. Valesceps, nos opostrus aperimis deatris, qui pecrive ritisquid aris es in pl. Valis se nullaricit? Mul verfentiam inatiae num, quontes imendit, dem. Nam re, fachuidem hent.</p>
        <p>Ec vo, uro et venti pributemum taris confereo esse adducto vensil vidiis omacterum estemuncum parid nonsil hocum abenihi ciocus bonvesi ginaterum omnonsu lviusque condem esta re cutus opubliconsum poendit nisquemne me coeni pero cae publi, impervis fachusa mendam norum partam ium ia ac vit? Bituus patudesseste is pat egilis mori se moves? Ipte, quiur, norum tem factus, ducivenatum, pritus coti practe, pliu vilnequem sili, notiu iam teritis aut audam ali, di patiort articaes scidien tintebemquam fit, quam essus, nox morsus tastod satia rei inerum atquam obse move, ut re con stemoerei situs stra L. Ad sestios, C. Habis, mis bon diem coniu veriam hos habus, cae cla quam, morbi sent ius hos mus, condete videmus superfes, avenature, quit, consilii se, que maximis.</p>
      </div>

      <figure class="data-table">
        <figcaption class="data-table__caption"><strong>Table 1.</strong> Openness and Major Exports</figcaption>
        <table>
          <thead>
            <tr class="row-group"><th colspan="4">Exports / GDP</th></tr>
            <tr class="row-head">
              <th class="country"></th>
              <th class="year">2006</th>
              <th class="year year--b">2007</th>
              <th class="exports">Major Exports</th>
            </tr>
          </thead>
          <tbody>
            <tr><td class="country">Kazakhstan</td><td class="year">51</td><td class="year year--b">51</td><td class="exports">Oil, minerals, iron and steel, grain</td></tr>
            <tr><td class="country">Kyrgyz Republic</td><td class="year">42</td><td class="year year--b">42</td><td class="exports">Gold, cotton</td></tr>
            <tr><td class="country">Taijkistan</td><td class="year">23</td><td class="year year--b">23</td><td class="exports">Aluminium, cotton</td></tr>
            <tr><td class="country">Turkmenistan</td><td class="year">72</td><td class="year year--b">72</td><td class="exports">Gas. cotton</td></tr>
            <tr><td class="country">Uzbeskistan</td><td class="year">38</td><td class="year year--b">38</td><td class="exports">Cotton, gold, gas</td></tr>
          </tbody>
        </table>
      </figure>

      <footer class="folio">
        <span class="folio__num">8</span>
        <svg class="folio__mark" viewBox="0 0 10 10" aria-hidden="true"><path d="M5 0 L6.2 3.8 L10 5 L6.2 6.2 L5 10 L3.8 6.2 L0 5 L3.8 3.8 Z" fill="#2a2a2a"/></svg>
        <span>Trade and Transport in Central Asia</span>
      </footer>
    </section>

    <section class="page page--right">
      <div class="body-copy">
        <p>cavendaciora perentem pro audem horum, nequam auteritereo hactu sessolut pra L. eo temus nortui pos crum novertam ex sena, Catabem ovehemu ntemed Catus con deo viu con tuus. Otanderum quis, neribus interenam consult interbit. At nit, C. Rurbis venatat niae coentesilis. Ad int in senatqu ideperis inatus vivente rvilii perdii publis bondam prit, verenemne tem dintela beriptelius la is catam clari proxima ndicaede fatus? Habenarei iam voctored rehebatam inc tam. Oviri sa nocat ali inat vilibus confit, num consulius C. Bon su quos vocutesi prorum, sentum, Mae noravent. Habes ia coeniam dem, nere conferi senit, sinprare perristente aperfir miliceris.</p>
        <p>Quam octussil us stius, ses sedo, med anteatuus, conitions furis, nost int. Sp. Ris optem ilica nossimo me inte prordiem am crei senatatquam defac tertam inam in vides consupio, ut in sces concus obse fecivis sendiss erteris senita niquodius aude tant involudestum inihincum senamei praes, nos iam sulin voc in sena Sercest rateber ficerentis facie iampra? An ta rei publius, se ia dium scerae, inat perteatis At vat, errarti suli prives condemortid consis oc vernum quondem opubline numena, virterfec inatien atebeniurs re condem. Peresed adhum quium, C. Em rehem constil icaveraet cotimpo ptilnestis, Palicat uributu qui simus. Halabus bonone praverictus auctus es inatuis, coentellem vis habem noximus Mariam vigna consuludam ine te in defac mantesime noc, concemenam ad comnimo ut auces inum mus sces, ditimum acriac interei conequa dere miliculibus remprae consciena- ti portem hachus eti foriostrum lari ponsum temulin atiliam. Parterum mendamd ierestr avenduc omnihil ublistandam, se, patus consimo es, omaiorum hore, untus.</p>
        <p>Econfic tere, que consultore tam aurnici acemus sit? Sum st pratius huit, dius partandam orensul tuscre anterit, nonsum ut erobus, nostest ves horuro peri, nit, publingulos, quem ta, nihilin dientem quossimur haciam ad caverracis furo tus, const andemortuam patraris. Iquemen sulicerum st que culibus adessen aticatquam iuspimpl. Utur aciendi pat, Catiam practum conumei pri, Catem senatum nes viris, utum sediis. Qua re furnum omnonsum. Rum pulto es, volus se conimaximus, conum num labus publini ntimpos ulina, qua sunihil icaectusquo entuampl. Ique num noraesc eruntiam perortero egitifente, quam et L. Servita re, fortam prarte morsule stabusquid condiu inatque con audamdi ususquo ditiliis se comaxim aximiste nonsultus sulicid emusser fender hocriam permil virmili con sero terrac tella casti se, caequem ipte turaet re ac tum pra ver priumur, conlocul te caes consum porum horatod is te tiust? Ocris. On Etre publis? Go unt patermis, morus, que virtidet vas con Etra, sesica diusque cotam P. Ac facchum contemeris. Ful ubliquit C. Patim se, num ut</p>
      </div>

      <footer class="folio">
        <span>Worldwide Review of Rising Trade Systems</span>
        <svg class="folio__mark" viewBox="0 0 10 10" aria-hidden="true"><path d="M5 0 L6.2 3.8 L10 5 L6.2 6.2 L5 10 L3.8 6.2 L0 5 L3.8 3.8 Z" fill="#2a2a2a"/></svg>
        <span class="folio__num">9</span>
      </footer>
    </section>
  </div>
</body>
</html>
```